Korvane Pty Ltd professional business card

A professional business card template using the colours from the supplied logo.
Clean crisp lines while, Modern while not being over the top.

Target Market(s)

Construction, commerical and industrial

Industry/Entity Type

Communications

Contact Information for Business Card

For a Communications, IT, Optical fibre installation company

Colors
37b8a4

```html
<!DOCTYPE html>
<html lang="en">
<head>
<meta charset="utf-8">
<title>Korvane Pty Ltd — Business Card</title>
<link href="https://fonts.googleapis.com/css2?family=Montserrat:wght@600;800&family=Arimo:wght@400&display=swap" rel="stylesheet">
<style>
  :root {
    --teal: #29b8a4;
    --teal-soft: #3bbfab;
    --teal-faint: #d5f0ec;
    --ink: #6a6a6e;
    --text: #4a4a4e;
    --paper: #ffffff;
    --backdrop: #dcdcdc;
  }
  html, body {
    margin: 0;
    width: 1200px;
    height: 900px;
    overflow: hidden;
    background: var(--backdrop);
  }
  .canvas {
    position: relative;
    width: 1200px;
    height: 900px;
  }
  .card {
    position: absolute;
    left: 250px;
    width: 700px;
    height: 400px;
    border-radius: 28px;
    overflow: hidden;
    box-shadow: 0 6px 18px rgba(0,0,0,0.18);
  }
  .card--front { top: 40px; background: var(--teal); }
  .card--back  { top: 460px; background: var(--paper); }

  .front-accent {
    position: absolute;
    right: -120px;
    top: -60px;
    width: 420px;
    height: 420px;
    border-radius: 50%;
    background: var(--teal-soft);
  }
  .front-wordmark {
    position: absolute;
    left: 0; right: 0;
    top: 165px;
    text-align: center;
    font-family: "Montserrat", sans-serif;
    font-weight: 600;
    font-size: 62px;
    letter-spacing: 6px;
    color: var(--paper);
  }

  .back-accent {
    position: absolute;
    right: -80px;
    top: 40px;
    width: 330px;
    height: 330px;
    border-radius: 50%;
    background: var(--teal-faint);
  }
  .back-tab {
    position: absolute;
    left: -18px;
    top: 228px;
    width: 36px;
    height: 44px;
    border-radius: 10px;
    background: var(--teal);
  }
  .back-wordmark {
    position: absolute;
    left: 60px;
    top: 58px;
    font-family: "Montserrat", sans-serif;
    font-weight: 600;
    font-size: 44px;
    letter-spacing: 4px;
    color: var(--ink);
  }
  .contact {
    position: absolute;
    left: 60px;
    top: 150px;
    font-family: "Arimo", Arial, sans-serif;
    color: var(--text);
    font-size: 15px;
    line-height: 1.35;
  }
  .contact__name {
    font-family: "Montserrat", sans-serif;
    font-weight: 800;
    font-size: 22px;
    letter-spacing: 1px;
    color: var(--teal);
    margin: 0;
  }
  .contact__role { margin: 2px 0 14px; font-size: 16px; }
  .contact__address { margin: 0 0 12px; }
  .contact__list { list-style: none; margin: 0; padding: 0; }
  .contact__list li { display: flex; align-items: center; gap: 8px; margin-bottom: 3px; }
  .contact__icon { width: 13px; height: 13px; flex: none; }
</style>
</head>
<body>
<main class="canvas">
  <section class="card card--front" aria-label="Card front">
    <div class="front-accent"></div>
    <div class="front-wordmark">KORVANE</div>
  </section>

  <section class="card card--back" aria-label="Card back">
    <div class="back-accent"></div>
    <div class="back-tab"></div>
    <div class="back-wordmark">KORVANE</div>
    <div class="contact">
      <p class="contact__name">DANA WHITLOW</p>
      <p class="contact__role">General Manager</p>
      <p class="contact__address">14 Harbourline Rd<br>Marlow Bay, CT 409318</p>
      <ul class="contact__list">
        <li>
          <svg class="contact__icon" viewBox="0 0 16 16" aria-hidden="true"><path fill="#29b8a4" d="M3.5 1.5l2.5 0 1 3.5-1.7 1.2a9 9 0 0 0 4.5 4.5L11 9l3.5 1v2.5c0 1-.8 1.8-1.8 1.8A11.2 11.2 0 0 1 1.7 3.3c0-1 .8-1.8 1.8-1.8z"/></svg>
          (512) 555-0147
        </li>
        <li>
          <svg class="contact__icon" viewBox="0 0 16 16" aria-hidden="true"><rect x="1" y="3" width="14" height="10" rx="1" fill="#29b8a4"/><path d="M1.5 3.5L8 9l6.5-5.5" stroke="#fff" stroke-width="1.3" fill="none"/></svg>
          contact@korvane.com.au
        </li>
        <li>
          <svg class="contact__icon" viewBox="0 0 16 16" aria-hidden="true"><circle cx="8" cy="8" r="6.5" fill="none" stroke="#29b8a4" stroke-width="1.4"/><ellipse cx="8" cy="8" rx="2.8" ry="6.5" fill="none" stroke="#29b8a4" stroke-width="1.2"/><path d="M1.5 8h13M2.5 5h11M2.5 11h11" stroke="#29b8a4" stroke-width="1"/></svg>
          www.korvane.com.au
        </li>
      </ul>
    </div>
  </section>
</main>
</body>
</html>
```